Flyer for an online formula one racing league

Hello.

I am looking for the perfect one page facebook/instagram style flyer for an online formula one racing league. The racing league is called 'VOLTA RACING LEAGUE'.

Information that MUST be on the new flyer is already on the old flyer I have uploaded here. In addition to including: The Volta racing league 'V' logo I have uploaded AND the text: 'Very popular, clean and competitive racing league, running for its 4th season. Why not join with a friend? Race times, Mondays, Tuesdays and Wednesdays each at 8pm UK TIME Message below for any questions. (Spacing of information is not important, however all the information in regards to the racing I have just mentioned MUST BE on the flyer, this includes info from old pic, logo and the other info I just mentioned).

It would be beneficial to have lots of dark blue on the flyer and the new flyer to be a lot different to the original flyer I uploaded, but this is not essential.

I apologise if I did not explain very well, any questions, please message me.

The best flyer should look the most attractive to someone that might be interested in joining an online formula one racing league.

I used this website before to create the perfect logo for my Sunday League team last year, and I was very impressed. I look forward to seeing your submissions.

Target Market(s)

No specific target, more something that may attract someone into joining a formula one online racing league

Industry/Entity Type

e sports/formula one

Colors
0054AA
0677BA
7BADD7
CADEEF
E8F1F8

Requirements
Must have
• Read product description please
Should not have
• Ignoring product description!

```html
<!DOCTYPE html>
<html lang="en">
<head>
<meta charset="utf-8">
<title>Volta Racing League – Season 4 Flyer</title>
<link rel="stylesheet" href="https://fonts.googleapis.com/css2?family=Anton&family=Poppins:ital,wght@0,400;0,500;0,600;0,700;0,800;1,700;1,800&display=swap">
<style>
  :root{
    --page:#ffffff;
    --ink-navy:#070b2a;
    --deep-navy:#0b1240;
    --hot-pink:#e5127d;
    --royal-blue:#1c14ea;
    --signal-yellow:#f4e500;
    --signal-green:#24d419;
    --white:#ffffff;
    --silver-light:#f4f4f6;
    --silver-mid:#b9bcc4;
    --silver-dark:#8a8d96;
  }
  *{margin:0;padding:0;box-sizing:border-box;}
  html,body{width:1200px;height:1200px;overflow:hidden;background:var(--page);}
  body{position:relative;font-family:"Poppins",sans-serif;}

  .flyer{
    position:absolute;left:60px;top:318px;width:1080px;height:564px;
    background:radial-gradient(ellipse at 50% 70%,#10163a 0%,var(--ink-navy) 70%);
    overflow:hidden;
  }
  .header-band{position:absolute;left:0;top:0;width:1080px;height:166px;background:var(--deep-navy);}
  .header-art{
    position:absolute;left:600px;top:0;width:480px;height:166px;
    background:radial-gradient(circle at 55% 45%,rgba(120,90,190,.55) 0%,rgba(40,60,150,.35) 35%,rgba(11,18,64,0) 70%);
  }
  .pink-corner{position:absolute;left:0;top:0;}

  .brand-mark{
    position:absolute;left:40px;top:6px;width:152px;height:152px;border-radius:50%;
    background:var(--deep-navy);border:4px solid var(--white);
    display:flex;align-items:center;justify-content:center;
    font-family:"Poppins",sans-serif;font-weight:700;font-size:92px;color:var(--white);line-height:1;
  }

  .league-title{position:absolute;left:200px;top:0;width:860px;height:166px;overflow:visible;}
  .league-title text{font-family:"Anton",sans-serif;font-size:130px;}

  .tagline-band{
    position:absolute;left:0;top:162px;width:1080px;height:63px;background:var(--royal-blue);
    color:var(--white);font-weight:500;font-size:30px;text-align:center;line-height:52px;
  }
  .tagline-rule{position:absolute;left:112px;top:212px;width:856px;height:6px;border-radius:3px;background:linear-gradient(180deg,#fff,#9da0a8);}

  .season-box{
    position:absolute;left:124px;top:218px;width:832px;height:72px;
    border:3px solid var(--silver-mid);border-top:none;border-radius:0 0 18px 18px;
    background:var(--ink-navy);
    display:flex;align-items:center;justify-content:center;gap:28px;
    font-weight:700;font-size:48px;color:var(--white);
  }
  .season-box .highlight{color:var(--signal-yellow);}
  .season-box sup{font-size:26px;vertical-align:22px;margin-right:10px;}

  .online-line{
    position:absolute;left:0;top:290px;width:1080px;height:64px;
    display:flex;align-items:center;justify-content:center;gap:12px;
    font-weight:500;font-size:46px;color:var(--white);letter-spacing:.5px;
  }
  .online-line .accent{color:var(--signal-green);}

  .divisions-band{position:absolute;left:46px;top:361px;width:992px;height:58px;}
  .divisions-band svg{position:absolute;inset:0;}
  .divisions-band p{
    position:absolute;inset:0;display:flex;align-items:center;justify-content:center;
    font-weight:800;font-style:italic;font-size:31px;color:var(--white);white-space:nowrap;
  }
  .divisions-band .count{color:var(--signal-yellow);margin-right:10px;}

  .invite{
    position:absolute;left:0;top:421px;width:1080px;text-align:center;
    font-weight:800;font-style:italic;font-size:40px;line-height:56px;
    background:linear-gradient(180deg,#ffffff 0%,#d9dbe0 50%,#9a9da5 100%);
    -webkit-background-clip:text;background-clip:text;color:transparent;
  }

  .race-times{
    position:absolute;left:40px;top:482px;width:1002px;height:46px;
    border:3px solid var(--white);border-radius:4px;background:var(--deep-navy);
    display:flex;align-items:stretch;
    font-weight:700;color:var(--white);white-space:nowrap;
  }
  .race-times .label{background:var(--hot-pink);width:196px;display:flex;align-items:center;justify-content:center;font-size:27px;clip-path:polygon(0 0,100% 0,96% 100%,0 100%);}
  .race-times .day{display:flex;align-items:center;justify-content:center;font-size:23px;font-weight:600;}
  .race-times .day--mon{width:152px;}
  .race-times .day--tue{width:172px;background:var(--royal-blue);clip-path:polygon(6% 0,100% 0,94% 100%,0 100%);}
  .race-times .day--wed{width:204px;}
  .race-times .time{flex:1;background:var(--hot-pink);position:relative;display:flex;align-items:center;justify-content:flex-end;padding-right:12px;font-size:29px;}
  .calendar-icon{position:absolute;left:-2px;top:-6px;width:52px;height:52px;border-radius:50%;background:var(--white);display:flex;align-items:center;justify-content:center;}
</style>
</head>
<body>
  <main class="flyer">
    <div class="header-band"></div>
    <div class="header-art" role="img" aria-label="Glowing speedometer dial and chequered racing graphics"></div>
    <svg class="pink-corner" width="170" height="166" viewBox="0 0 170 166" aria-hidden="true">
      <polygon points="0,0 44,0 160,166 0,166" fill="var(--hot-pink)"/>
    </svg>

    <div class="brand-mark" aria-label="Volta Racing League">V</div>

    <svg class="league-title" viewBox="0 0 860 166" role="heading" aria-level="1" aria-label="VOLTA RACING LEAGUE">
      <defs>
        <linearGradient id="title-silver" x1="0" y1="0" x2="0" y2="1">
          <stop offset="0" stop-color="#f4f4f6"/>
          <stop offset="0.45" stop-color="#ffffff"/>
          <stop offset="0.58" stop-color="#b9bcc4"/>
          <stop offset="1" stop-color="#8a8d96"/>
        </linearGradient>
      </defs>
      <text x="36" y="134" transform="skewX(-10)" textLength="810" lengthAdjust="spacingAndGlyphs" fill="url(#title-silver)">VOLTA RACING LEAGUE</text>
    </svg>

    <p class="tagline-band">Very popular, clean and competitive racing league</p>
    <div class="tagline-rule"></div>

    <div class="season-box">
      <span>RUNNING FOR ITS</span>
      <span class="highlight">4<sup>TH</sup>SEASON</span>
    </div>

    <p class="online-line">
      <svg width="40" height="40" viewBox="0 0 40 40" aria-hidden="true">
        <rect x="1.5" y="1.5" width="37" height="37" fill="none" stroke="#fff" stroke-width="3"/>
        <line x1="1.5" y1="9" x2="38.5" y2="9" stroke="#fff" stroke-width="2"/>
        <path d="M6 32 A14 14 0 0 1 34 32" fill="none" stroke="#fff" stroke-width="3"/>
        <line x1="20" y1="32" x2="28" y2="21" stroke="#fff" stroke-width="3"/>
      </svg>
      <span>CLEAN <span class="accent">ONLINE</span> RACING LEAGUE</span>
    </p>

    <div class="divisions-band">
      <svg width="992" height="58" viewBox="0 0 992 58" aria-hidden="true">
        <polygon points="14,0 978,0 992,58 0,58" fill="#d6d8de"/>
        <polygon points="30,0 962,0 976,58 16,58" fill="var(--hot-pink)"/>
      </svg>
      <p><span class="count">3 DIVISIONS</span> CURRENTLY AND LOOKING TO KEEP GROWING!</p>
    </div>

    <p class="invite">Why not join with a friend?</p>

    <div class="race-times">
      <span class="label">RACE TIMES</span>
      <span class="day day--mon">MONDAYS</span>
      <span class="day day--tue">TUESDAYS</span>
      <span class="day day--wed">WEDNESDAYS</span>
      <span class="time">
        <span class="calendar-icon">
          <svg width="28" height="28" viewBox="0 0 28 28" aria-hidden="true">
            <rect x="2" y="5" width="22" height="20" rx="3" fill="none" stroke="var(--hot-pink)" stroke-width="2.5"/>
            <rect x="2" y="5" width="22" height="6" fill="var(--hot-pink)"/>
            <rect x="7" y="14" width="3" height="3" fill="var(--hot-pink)"/>
            <rect x="12" y="14" width="3" height="3" fill="var(--hot-pink)"/>
            <rect x="7" y="19" width="3" height="3" fill="var(--hot-pink)"/>
            <circle cx="21" cy="21" r="5" fill="#fff" stroke="var(--hot-pink)" stroke-width="2"/>
          </svg>
        </span>
        8PM UK TIME
      </span>
    </div>
  </main>
</body>
</html>
```